依頼詳細
今回は」取り急ぎ3種類の用途のメッセージカードのデザイン作成の依頼です。
メッセージカードに入れる文章も決まっていますのでその内容も入れての作成をお願いします。追加の依頼として14種類のメッセージカードの依頼もありますのでよろしくお願いします。
記載項目
株式会社マツバネ贈答
担当:田辺
TEL025-275-1277 FAX025-275-1350
Email:kenji@matsubanezoto.example.jp
希望イメージ
シンプル 複雑
単色 カラフル
暗い 明るい
日常 高級
遊び心 厳粛
未来的 伝統的
女性的 男性的
希望する色
設定なし
納品ファイル
• イラストレーター形式 (.ai)
• フォトショップ形式 (.psd)
• PNG形式 (.png)
補足説明
メッセージカードに入れる文章を添付しますので、よろしくお願いします。
また、参考までに今現在使用しているメッセージカードを添付します。
全く違うイメージでOKです。逆に異なった方がいいです。
サイズ:B7サイズ 91 × 128 ミリ
■ 選んだ理由

ご用途に合った上品なデザインが素敵でした。
年配の方への贈り物が多いので、特に還暦・長寿が派手過ぎず華やかで好感が持てました。

■ 提案者全員のお礼・コメント

たくさんのご提案をいただき、誠にありがとうございました。
どれも素敵なデザインでしたので選出にかなり迷いました。
他の用途でも依頼が出来たらと思いますので、またご縁がございましたらよろしくお願い致します。

```html
<!DOCTYPE html>
<html lang="ja">
<head>
<meta charset="utf-8">
<title>退職祝 メッセージカード</title>
<link rel="stylesheet" href="https://fonts.googleapis.com/css2?family=Shippori+Mincho+B1:wght@500;800&display=swap">
<style>
  :root {
    --paper: #ffffff;
    --ink: #2a2224;
    --rose: #d9607a;
    --rose-soft: #f3c6d0;
    --ribbon: #e0738a;
    --trim: #555555;
    --wood-dark: #4a3426;
    --wood-mid: #8a6a50;
    --kraft-light: #d9c3a8;
  }
  * { margin: 0; padding: 0; box-sizing: border-box; }
  html, body {
    width: 857px; height: 1200px; overflow: hidden;
    background: var(--paper);
  }
  .sheet { position: relative; width: 857px; height: 1200px; }
  .trim-marks { position: absolute; inset: 0; }
  .card {
    position: absolute; left: 143px; top: 200px;
    width: 571px; height: 786px;
    background: var(--paper);
    overflow: hidden;
  }
  .card-photo {
    position: absolute; left: 0; top: 0; width: 100%; height: 450px;
    background: linear-gradient(180deg, var(--wood-dark) 0%, var(--wood-mid) 45%, var(--kraft-light) 75%, var(--paper) 100%);
  }
  .ribbon-corner { position: absolute; inset: 0; width: 100%; height: 100%; }
  .title-band {
    position: absolute; left: 0; top: 453px; width: 100%; height: 12px;
    background: var(--ribbon);
  }
  .title-heart { position: absolute; left: 225px; top: 395px; width: 122px; height: 110px; }
  .title {
    position: absolute; left: 0; top: 405px; width: 100%;
    text-align: center;
    font-family: "Shippori Mincho B1", serif;
    font-weight: 800; font-size: 54px; line-height: 1.2; letter-spacing: 2px;
    color: var(--rose);
    text-shadow: 0 0 4px #fff, 0 0 4px #fff, 0 0 6px #fff;
  }
  .message {
    position: absolute; left: 0; top: 530px; width: 100%;
    text-align: center;
    font-family: "Shippori Mincho B1", serif;
    font-weight: 500; font-size: 23px; line-height: 37px;
    color: var(--ink);
  }
</style>
</head>
<body>
<div class="sheet">
  <svg class="trim-marks" width="857" height="1200" viewBox="0 0 857 1200" fill="none" stroke="var(--trim)" stroke-width="1.5">
    <path d="M60 117 H143 M114 117 V0 M143 117 V60 M60 146 H114"/>
    <path d="M797 117 H714 M743 117 V0 M714 117 V60 M797 146 H743"/>
    <path d="M60 1069 H143 M114 1069 V1200 M143 1069 V1140 M60 1040 H114"/>
    <path d="M797 1069 H714 M743 1069 V1200 M714 1069 V1140 M797 1040 H743"/>
    <path d="M428 88 V146 M330 117 H526"/>
    <path d="M428 1040 V1098 M330 1069 H526"/>
    <path d="M85 593 H143 M114 495 V691"/>
    <path d="M714 593 H772 M743 495 V691"/>
  </svg>

  <section class="card">
    <div class="card-photo" role="img" aria-label="木のテーブルに置かれたリボン付きの贈り物と花束の写真"></div>
    <svg class="ribbon-corner" viewBox="0 0 571 786">
      <polygon points="0,70 70,0 110,0 0,110" fill="var(--ribbon)"/>
      <polygon points="571,680 465,786 505,786 571,720" fill="var(--ribbon)"/>
    </svg>
    <div class="title-band"></div>
    <svg class="title-heart" viewBox="0 0 122 110">
      <path d="M61 106 C10 70 0 45 0 28 C0 10 15 0 31 0 C45 0 55 9 61 20 C67 9 77 0 91 0 C107 0 122 10 122 28 C122 45 112 70 61 106 Z" fill="var(--rose-soft)"/>
    </svg>
    <h1 class="title">退職祝</h1>
    <p class="message">
      ご退職おめでとうございます。<br>
      感謝の気持ちを込めて、<br>
      ささやかな「記念品」をお贈りさせて<br>
      いただきます。<br>
      ご笑納頂ければ幸いです。
    </p>
  </section>
</div>
</body>
</html>
```